Fun but corporate B2B Infographic

Infographic - for use on corporate [B2B] web site: https://www.vextrano.com/ +++++++++++++++Title of infographic: VEXTRANO, by the numbers- 7,322 Active users from - 61 different countries [1/3rd of the world] running- 14.8 million report calculations returning 6.5 Billion data points at an average of4.1 seconds to render a report - from request to presentation using reports developed with52 specialist Celvo functions surfaced in3 Brindle Suite Applications [Celvo – Slidemaker – Scriba] and across ALL web browsers All this wrapped in an All-In-One platform for Reporting, Business Intelligence, Budgeting and Forecasting.++++++++++++Will need 2x rounds of revisions - and preferably provide final artwork files for us to make tweaks to in the future.Use the images/logos and style guide attached.

Target Market(s)

CFOs and Financial controllers

Font styles to use
Sans Serif

Colors

Designer to choose colors to be used in the design.

Requirements
Must have
• graphics, fun icons matching the words - eg: we say "1/3rd of the world", so put an image of a globe or a map with the major countries identified/different colour.
• Although this is B2B, it also needs to be eye-catching and fun

```html
<!DOCTYPE html>
<html lang="en">
<head>
<meta charset="utf-8">
<title>VEXTRANO by the numbers 2018-2019</title>
<link href="https://fonts.googleapis.com/css2?family=Fira+Sans+Condensed:wght@400;600;700&family=Fira+Sans:wght@400;600;700&display=swap" rel="stylesheet">
<style>
:root{
  --navy:#0a2a66;
  --navy-deep:#062259;
  --green:#8cc63f;
  --white:#ffffff;
  --ink:#111111;
  --header:#f3f3f3;
  --stage:#cfe3f8;
  --disc-dark:#1b3d80;
  --disc-light:#e3e8f0;
  --globe:#9fbcd6;
  --app-blue:#3b5ea8;
  --app-red:#c8502e;
  --app-green:#23783f;
}
*{margin:0;padding:0;box-sizing:border-box}
html,body{width:1200px;height:949px;overflow:hidden;background:var(--stage)}
body{position:relative;font-family:"Fira Sans Condensed","Fira Sans",sans-serif}
.sheet{position:absolute;top:51px;width:534px;height:850px;background:var(--navy);overflow:hidden;box-shadow:0 6px 16px rgba(40,70,110,.25)}
.sheet--dark{left:49px}
.sheet--light{left:610px;background:var(--white)}
.sheet__head{position:absolute;left:0;top:0;width:100%;height:80px;background:var(--header)}
.brand{position:absolute;left:15px;top:18px;display:flex;align-items:center;gap:10px}
.brand__mark{width:44px;height:44px;border-radius:50%;background:var(--green)}
.brand__name{font-family:"Fira Sans",sans-serif;font-weight:700;font-size:36px;color:var(--navy);letter-spacing:.5px;line-height:1}
.period{position:absolute;right:36px;top:32px;font-family:"Fira Sans",sans-serif;font-size:25px;color:var(--navy)}
.t{position:absolute;white-space:nowrap;font-weight:600;line-height:1;letter-spacing:-.6px;color:var(--white)}
.sheet--light .t{color:var(--navy)}
.sheet--light .t--ink{color:var(--ink)}
.t--green,.sheet--light .t--green{color:var(--green)}
.disc{position:absolute;border-radius:50%}
.sheet--dark .disc{background:var(--disc-dark)}
.sheet--light .disc{background:var(--disc-light)}
.sheet--dark .disc--globe{background:radial-gradient(circle at 45% 45%,var(--globe) 0 45%,transparent 46%),var(--disc-dark)}
.sheet--light .disc--globe{background:radial-gradient(circle at 45% 45%,var(--globe) 0 45%,transparent 46%),var(--disc-light)}
.sheet .disc--watch{background:var(--disc-light);border:5px solid var(--navy)}
.sheet--dark .disc--watch{border-color:var(--white)}
.chart{position:absolute}
.apps{position:absolute;left:55px;top:677px;display:flex;gap:14px}
.sheet--light .apps{left:46px}
.apps span{width:56px;height:56px;border-radius:6px}
.apps .a1{background:var(--app-blue)}
.apps .a2{background:var(--app-red)}
.apps .a3{background:var(--app-green)}
.sheet__foot{position:absolute;left:0;bottom:0;width:100%;height:43px;background:var(--header);display:flex;align-items:center;justify-content:center;font-family:"Fira Sans",sans-serif;font-weight:600;font-size:23px;color:var(--navy);letter-spacing:.3px}
.sheet--light .sheet__foot{background:var(--navy-deep);color:var(--white)}
.sheet__foot i{font-style:normal;color:var(--green);margin:0 10px;font-size:14px}
.over{transform:rotate(-90deg);transform-origin:left top}
</style>
</head>
<body>

<section class="sheet sheet--dark">
  <header class="sheet__head">
    <div class="brand"><span class="brand__mark"></span><span class="brand__name">VEXTRANO</span></div>
    <div class="period">2018-2019</div>
  </header>

  <div class="disc disc--globe" role="img" aria-label="Globe with one third of the world highlighted" style="left:403px;top:112px;width:122px;height:122px"></div>
  <div class="t t--green" style="left:238px;top:140px;font-size:72px;font-weight:700">61</div>
  <div class="t" style="left:303px;top:146px;font-size:28px">different</div>
  <div class="t" style="left:303px;top:172px;font-size:28px">countries</div>

  <div class="disc" role="img" aria-label="Report sheet with charts and a calculator" style="left:13px;top:237px;width:162px;height:162px"></div>
  <div class="t" style="left:40px;top:178px;font-size:30px">running</div>
  <div class="t t--green" style="left:106px;top:201px;font-size:52px">14.8</div>
  <div class="t" style="left:201px;top:217px;font-size:30px">million</div>
  <div class="t" style="left:161px;top:250px;font-size:38px">report</div>
  <div class="t" style="left:153px;top:285px;font-size:31px">calculations</div>

  <svg class="chart" style="left:448px;top:290px" width="42" height="72" viewBox="0 0 42 72">
    <polyline points="4,68 8,42 25,32 34,6" fill="none" stroke="#8cc63f" stroke-width="3"/>
    <circle cx="25" cy="32" r="4" fill="#8cc63f"/><circle cx="34" cy="6" r="4" fill="#8cc63f"/>
  </svg>
  <div class="t over" style="left:267px;top:421px;font-size:24px">Over</div>
  <div class="t t--green" style="left:291px;top:351px;font-size:44px">6.5&nbsp;&nbsp;Billion</div>
  <div class="t" style="left:291px;top:384px;font-size:40px">data points</div>
  <div class="t" style="left:293px;top:418px;font-size:31px">stored</div>

  <div class="t" style="left:21px;top:461px;font-size:21px">at an average of</div>
  <div class="t t--green" style="left:21px;top:475px;font-size:38px">4.1 seconds</div>
  <div class="t" style="left:21px;top:507px;font-size:23px">to render a report</div>
  <div class="disc disc--watch" role="img" aria-label="Stopwatch" style="left:215px;top:463px;width:70px;height:70px"></div>

  <div class="disc" role="img" aria-label="Group of business people" style="left:401px;top:499px;width:112px;height:112px"></div>
  <div class="t" style="left:212px;top:559px;font-size:31px">developed</div>
  <div class="t t--green" style="left:358px;top:560px;font-size:44px">52</div>
  <div class="t" style="left:326px;top:589px;font-size:15px">with</div>
  <div class="t" style="left:326px;top:600px;font-size:19px">specialist</div>
  <div class="t" style="left:270px;top:620px;font-size:20px">Celvo functions in</div>

  <div class="apps"><span class="a1"></span><span class="a2"></span><span class="a3"></span></div>
  <div class="t t--green" style="left:259px;top:668px;font-size:42px">3 Brindle</div>
  <div class="t" style="left:259px;top:709px;font-size:25px"><span style="color:var(--green);font-size:28px">Suite</span> applications</div>
  <div class="t" style="left:45px;top:735px;font-size:35px">and across <span style="color:var(--green)">ALL web browsers</span></div>

  <footer class="sheet__foot">PREDICT<i>●</i>SHAPE<i>●</i>ACHIEVE</footer>
</section>

<section class="sheet sheet--light">
  <header class="sheet__head">
    <div class="brand"><span class="brand__mark"></span><span class="brand__name">VEXTRANO</span></div>
    <div class="period">2018-2019</div>
  </header>

  <div class="disc disc--globe" role="img" aria-label="Globe with one third of the world highlighted" style="left:405px;top:108px;width:122px;height:122px"></div>
  <div class="t" style="left:242px;top:136px;font-size:72px;font-weight:700">61</div>
  <div class="t t--ink" style="left:307px;top:142px;font-size:28px">different</div>
  <div class="t t--ink" style="left:307px;top:168px;font-size:28px">countries</div>

  <div class="disc" role="img" aria-label="Report sheet with charts and a calculator" style="left:14px;top:233px;width:162px;height:162px"></div>
  <div class="t t--ink" style="left:44px;top:176px;font-size:30px">running</div>
  <div class="t t--green" style="left:110px;top:199px;font-size:52px">14.8</div>
  <div class="t t--ink" style="left:210px;top:216px;font-size:30px">million</div>
  <div class="t" style="left:156px;top:240px;font-size:44px">report</div>
  <div class="t" style="left:156px;top:282px;font-size:31px">calculations</div>

  <svg class="chart" style="left:444px;top:308px" width="50" height="46" viewBox="0 0 50 46">
    <polyline points="4,42 12,26 30,24 44,6" fill="none" stroke="#b8c2d2" stroke-width="3"/>
    <circle cx="12" cy="26" r="4" fill="#0a2a66"/><circle cx="30" cy="24" r="4" fill="#0a2a66"/><circle cx="44" cy="6" r="4" fill="#0a2a66"/>
  </svg>
  <div class="t t--ink over" style="left:264px;top:420px;font-size:24px">Over</div>
  <div class="t t--green" style="left:289px;top:350px;font-size:44px">6.5&nbsp;&nbsp;Billion</div>
  <div class="t" style="left:289px;top:383px;font-size:40px">data points</div>
  <div class="t t--ink" style="left:291px;top:417px;font-size:31px">stored</div>

  <div class="t t--ink" style="left:25px;top:463px;font-size:21px">at an average of</div>
  <div class="t t--green" style="left:25px;top:477px;font-size:38px">4.1 seconds</div>
  <div class="t t--ink" style="left:25px;top:509px;font-size:23px">to render a report</div>
  <div class="disc disc--watch" role="img" aria-label="Stopwatch" style="left:218px;top:463px;width:70px;height:70px"></div>

  <div class="disc" role="img" aria-label="Group of business people" style="left:396px;top:500px;width:112px;height:112px"></div>
  <div class="t t--ink" style="left:207px;top:561px;font-size:31px">developed</div>
  <div class="t t--green" style="left:354px;top:562px;font-size:44px">52</div>
  <div class="t" style="left:322px;top:591px;font-size:15px">with</div>
  <div class="t" style="left:322px;top:602px;font-size:19px">specialist</div>
  <div class="t t--ink" style="left:265px;top:622px;font-size:20px">Celvo functions in</div>

  <div class="apps"><span class="a1"></span><span class="a3"></span><span class="a2"></span></div>
  <div class="t t--green" style="left:247px;top:665px;font-size:42px">3 Brindle</div>
  <div class="t" style="left:247px;top:705px;font-size:25px"><span style="color:var(--green);font-size:28px">Suite</span> applications</div>
  <div class="t" style="left:45px;top:735px;font-size:35px">and across <span style="color:var(--green)">ALL web browsers</span></div>

  <footer class="sheet__foot">PREDICT<i>●</i>SHAPE<i>●</i>ACHIEVE</footer>
</section>

</body>
</html>
```